Business Consulting Business Card

professional business card with basic information (1) First and Last name (2) email address, (3) phone number, (4) website.

```html
<!DOCTYPE html>
<html lang="en">
<head>
<meta charset="utf-8">
<title>Tide Hollow – Business Card</title>
<link rel="stylesheet" href="https://fonts.googleapis.com/css2?family=Montserrat:ital,wght@0,400;0,700;1,400&display=swap">
<style>
  :root {
    --backdrop: #55b4c3;
    --card: #ffffff;
    --brand-teal: #55b4c3;
    --sea-top: #86bcc0;
    --sea-mid: #96ccd3;
    --sea-deep: #4f9eab;
    --ink-navy: #0d2b3e;
    --ink-black: #0a0a0a;
    --ink-dark: #1a1a1a;
  }
  * { box-sizing: border-box; margin: 0; padding: 0; }
  html, body { width: 1200px; height: 1200px; overflow: hidden; }
  body {
    background: var(--backdrop);
    font-family: "Montserrat", sans-serif;
    position: relative;
  }
  .card {
    position: absolute;
    left: 194px;
    width: 812px;
    height: 464px;
    background: var(--card);
    border-radius: 56px;
    overflow: hidden;
    box-shadow: 0 6px 24px rgba(20, 70, 85, 0.35);
  }
  .card--front { top: 110px; }
  .card--back { top: 611px; }

  /* Front */
  .front-brand {
    position: absolute;
    left: 0;
    right: 0;
    top: 150px;
    display: flex;
    justify-content: center;
    align-items: center;
    gap: 24px;
  }
  .brand-dot {
    width: 80px;
    height: 80px;
    border-radius: 50%;
    background: var(--brand-teal);
    flex: none;
  }
  .front-brand .brand-name {
    font-size: 40px;
    font-weight: 400;
    letter-spacing: 0.24em;
    margin-right: -0.24em;
    color: var(--ink-navy);
    white-space: nowrap;
  }
  .sea-band {
    position: absolute;
    left: 0;
    right: 0;
    top: 330px;
    bottom: 0;
    background: linear-gradient(180deg, var(--sea-top) 0%, var(--sea-mid) 45%, var(--sea-deep) 100%);
  }
  .front-url {
    position: absolute;
    left: 0; right: 0;
    top: 425px;
    text-align: center;
    font-size: 18px;
    font-style: italic;
    letter-spacing: 0.24em;
    color: #ffffff;
  }

  /* Back */
  .person-name {
    position: absolute;
    left: 85px;
    top: 96px;
    font-size: 43px;
    font-weight: 700;
    color: var(--ink-black);
    letter-spacing: -0.01em;
  }
  .person-role {
    position: absolute;
    left: 85px;
    top: 145px;
    font-size: 17px;
    font-style: italic;
    color: var(--ink-dark);
  }
  .contact-list {
    position: absolute;
    left: 82px;
    top: 235px;
    list-style: none;
  }
  .contact-item {
    display: flex;
    align-items: center;
    height: 26px;
    margin-bottom: 15px;
    font-size: 20px;
    color: var(--ink-dark);
  }
  .contact-icon {
    width: 26px; height: 26px;
    border-radius: 50%;
    background: var(--brand-teal);
    margin-right: 13px;
    flex: none;
    display: flex; align-items: center; justify-content: center;
  }
  .divider {
    position: absolute;
    left: 486px;
    top: 183px;
    width: 4px;
    height: 99px;
    background: var(--brand-teal);
  }
  .back-brand {
    position: absolute;
    left: 532px;
    width: 220px;
    top: 158px;
    display: flex;
    flex-direction: column;
    align-items: center;
    gap: 20px;
  }
  .back-brand .brand-dot { width: 96px; height: 96px; }
  .back-brand .brand-name {
    font-size: 20px;
    font-weight: 400;
    letter-spacing: 0.26em;
    margin-right: -0.26em;
    color: var(--ink-navy);
    white-space: nowrap;
  }
</style>
</head>
<body>

<section class="card card--front" aria-label="Card front">
  <div class="front-brand">
    <span class="brand-dot" aria-hidden="true"></span>
    <span class="brand-name">TIDE HOLLOW</span>
  </div>

  <div class="sea-band" role="img" aria-label="Decorative layered sea waves in teal tones"></div>

  <p class="front-url">www.tidehollow.com</p>
</section>

<section class="card card--back" aria-label="Card back">
  <h1 class="person-name">Daniel Reyes</h1>
  <p class="person-role">Brand Manager</p>

  <ul class="contact-list">
    <li class="contact-item">
      <span class="contact-icon" aria-hidden="true">
        <svg width="14" height="14" viewBox="0 0 24 24" fill="none" stroke="#fff" stroke-width="2" stroke-linecap="round" stroke-linejoin="round"><path d="M5 3h4l2 5-2.5 1.5a11 11 0 0 0 6 6L16 13l5 2v4a2 2 0 0 1-2 2A16 16 0 0 1 3 5a2 2 0 0 1 2-2z"/></svg>
      </span>
      <span>+12 555 010 42 42</span>
    </li>
    <li class="contact-item">
      <span class="contact-icon" aria-hidden="true">
        <svg width="14" height="14" viewBox="0 0 24 24" fill="none" stroke="#fff" stroke-width="1.8" stroke-linejoin="round"><rect x="3" y="5" width="18" height="14" rx="1"/><path d="M3 6l9 7 9-7M3 18l7-6M21 18l-7-6"/></svg>
      </span>
      <span>reyes-daniel@tidehollow.com</span>
    </li>
    <li class="contact-item">
      <span class="contact-icon" aria-hidden="true">
        <svg width="15" height="15" viewBox="0 0 24 24" fill="none" stroke="#fff" stroke-width="1.6"><circle cx="12" cy="12" r="9"/><ellipse cx="12" cy="12" rx="4" ry="9"/><path d="M3 12h18M5 7h14M5 17h14"/></svg>
      </span>
      <span>www.tidehollow.com</span>
    </li>
  </ul>

  <span class="divider" aria-hidden="true"></span>

  <div class="back-brand">
    <span class="brand-dot" aria-hidden="true"></span>
    <span class="brand-name">TIDE HOLLOW</span>
  </div>
</section>

</body>
</html>
```